business card and stationary pest control company
Bugwarden
business card and stationary pest control company - Cleaning
Creative Brief
Bright & Fun-filled
Malcolm Teague
General Manager
to be added
info@bugwarden.example
bugwarden.example
tarloq tarloq
Hi guys, please bear in mind it's a full stationary project, letterhead, fax, email, envelope etc ...
ravenmoss ravenmoss
check your private messages on top right! thankyou

```html
<!DOCTYPE html>
<html lang="en">
<head>
<meta charset="utf-8">
<title>Bugwarden – Business Card</title>
<link href="https://fonts.googleapis.com/css2?family=Ubuntu:wght@400;500;700&display=swap" rel="stylesheet">
<style>
  :root {
    --navy: #1f2f8f;
    --red: #d8232a;
    --ink: #2b2b3a;
    --muted: #6b6f7c;
    --card: #ffffff;
    --backdrop: #3a3b3e;
  }
  * { margin: 0; padding: 0; box-sizing: border-box; }
  html, body { width: 1200px; height: 782px; overflow: hidden; }
  body {
    background: var(--backdrop);
    font-family: "Ubuntu", Arial, sans-serif;
    position: relative;
  }
  .card {
    position: absolute;
    width: 540px;
    height: 309px;
    background: var(--card);
    border-radius: 18px;
    overflow: hidden;
    top: 236px;
  }
  .card--back { left: 40px; }
  .card--front { left: 620px; }
  .card__swoosh { position: absolute; inset: 0; width: 100%; height: 100%; }
  .brand {
    position: absolute;
    display: flex;
    align-items: center;
    gap: 8px;
  }
  .brand__dot {
    width: 16px; height: 16px; border-radius: 50%;
    background: var(--red);
    flex: none;
  }
  .brand__name {
    font-weight: 700;
    font-size: 34px;
    color: var(--navy);
    letter-spacing: -0.5px;
    line-height: 1;
  }
  .card--back .brand { left: 150px; top: 152px; }
  .card--front .brand { left: 40px; top: 162px; }
  .holder {
    position: absolute;
    right: 28px; top: 22px;
    text-align: right;
    color: #fff;
  }
  .holder__name { font-weight: 500; font-size: 17px; }
  .holder__role { font-size: 14px; margin-top: 2px; }
  .contact {
    position: absolute;
    left: 300px; top: 140px;
    padding-left: 14px;
    border-left: 1.5px solid var(--muted);
    font-size: 13px;
    color: var(--ink);
    line-height: 1.5;
  }
  .contact__line { display: flex; align-items: center; gap: 6px; white-space: nowrap; }
  .contact__icon { width: 12px; height: 12px; fill: var(--navy); flex: none; }
</style>
</head>
<body>

  <section class="card card--back" aria-label="Business card back">
    <svg class="card__swoosh" viewBox="0 0 540 309" aria-hidden="true">
      <path d="M0,0 H540 V105 C430,52 260,26 0,22 Z" fill="var(--navy)"/>
      <path d="M0,38 C220,38 420,66 540,124" fill="none" stroke="var(--red)" stroke-width="6"/>
    </svg>
    <div class="brand">
      <span class="brand__dot"></span><span class="brand__name">Bugwarden</span>
    </div>
  </section>

  <section class="card card--front" aria-label="Business card front">
    <svg class="card__swoosh" viewBox="0 0 540 309" aria-hidden="true">
      <path d="M0,0 H540 V105 C430,52 260,26 0,22 Z" fill="var(--navy)"/>
      <path d="M0,38 C220,38 420,66 540,124" fill="none" stroke="var(--red)" stroke-width="6"/>
    </svg>
    <div class="holder">
      <div class="holder__name">Dorian Felsby</div>
      <div class="holder__role">Consultant</div>
    </div>
    <div class="brand">
      <span class="brand__dot"></span><span class="brand__name">Bugwarden</span>
    </div>
    <div class="contact">
      <div class="contact__line">214, 6th floor, Harbor Lane</div>
      <div class="contact__line">Road QRT</div>
      <div class="contact__line">
        <svg class="contact__icon" viewBox="0 0 12 12" aria-hidden="true"><path d="M2.5 0.5l2 2-1 1.5c.7 1.5 1.8 2.6 3.3 3.3l1.5-1 2 2-1.3 2C5 11.8.2 7 .5 1.8z"/></svg>
        555 014 2290
      </div>
      <div class="contact__line">
        <svg class="contact__icon" viewBox="0 0 12 12" aria-hidden="true"><rect x="3" y="0" width="6" height="12" rx="1"/></svg>
        555 014 2290
      </div>
      <div class="contact__line">
        <svg class="contact__icon" viewBox="0 0 12 12" aria-hidden="true"><path d="M0 2h12v8H0z M0.8 2.6L6 6.6l5.2-4" stroke="#fff" stroke-width="0.8"/></svg>
        name@bugwarden.example
      </div>
      <div class="contact__line">www.bugwarden.example</div>
    </div>
  </section>

</body>
</html>
```